VelaMarina Passport 4 Page A5 Brochure

DESIGN BRIEF – VelaMarina Passport Brochure
Project Title
VelaMarina Passport – A5 4-Page Brochure Design
________________________________________
Overview
We are looking for a designer to create a clean, visually appealing A5, 4-page brochure to present The VelaMarina Passport to local businesses.
The brochure will be used as a sales and information document and should feel:
• Premium
• Friendly
• Professional
• Easy to understand
• Fun and engaging
The audience is bar owners, venue managers, restaurants, clubs, hotels, and local businesses in Maspalomas.
Format & Technical Requirements
• Size: A5
• Pages: 4 (front cover, 2 inside pages, back cover)
• Orientation: Portrait
• Print-ready design
• Space-aware layouts (some content will be added later)
Brand & Tone
• Brand: VelaMarina
• Location: Maspalomas / Gran Canaria
• Target audience: LGBTQ+ friendly venues and tourism businesses
• Style:
o Modern
o Warm
o Professional
o Island-inspired
o Not overly corporate
• Avoid clutter — white space is welcome
PAGE-BY-PAGE REQUIREMENTS
PAGE 1 – FRONT COVER
Purpose: First impression & visual impact
Requirements:
• Strong visual design
• Clear title: “The VelaMarina Passport”
• Subheading example:
A premium voucher booklet connecting tourists with local venues
• Leave a clear placeholder space for:
o An image of the Passport front cover
• We are open to designers also proposing a design for the Passport front cover itself (optional extra – happy to receive bids for this)
Style notes:
• Eye-catching but elegant
• Feel of travel, discovery, nightlife, and local culture
PAGE 2 – INSIDE LEFT
Purpose: Explain the concept – text provided
Content:
• Short overview of:
o What The VelaMarina Passport is
o Targeted distribution
o Key benefits (high-value visitors, no wasted reach, transferable, no expiry)
• Icons or visual blocks encouraged
• Easy-to-scan layout
Design Notes:
• Use headings, icons, or info blocks
• Avoid large walls of text
PAGE 3 – INSIDE RIGHT (How the Passport Works in Practice)
Purpose:
To visually explain how The VelaMarina Passport is owned, transferred, and used, while showing real examples of how venues appear inside the booklet.
Required Elements
1. Passport Ownership & Transfer Section
The Passport can be owned by up to three people in total (original owner + two transfers).
This page should include three clearly defined visual placeholders representing:
• Original Passport Owner
• Transfer 1 – New Owner
• Transfer 2 – Final Owner
These can be shown as:
• Three mini page mockups
• Three outlined boxes with headings
• Or a creative, passport-style visual layout
Each section should clearly show space for:
• Name
• Country (optional)
• Signature
• Date
👉 We are open to creative proposals for the design of this transfer page and happy to receive bids specifically for designing this page as part of the Passport.
2. Example Voucher Advert Section
This page should also include space to show an example of a voucher advert page, displayed as a mock layout only.
The example should visually communicate:
• Venue name & logo
• Short venue description
• Example offer (e.g. “Free signature shot”)
• Voucher box to be crossed off by staff
This is illustrative only — final content will be provided later.
Design Notes
• Keep the layout clear and easy to understand at a glance
• Visual explanation is more important than text
• Use icons, borders, or soft background panels to separate sections
• The tone should feel official but friendly, similar to a real passport
• Avoid clutter — white space is encouraged
Key Message to Communicate Visually
• The Passport has real ownership
• It can be passed on
• Vouchers are clearly controlled
• Each page feels premium, structured, and easy to use
PAGE 4 – BACK COVER
Purpose: Commercial offer & call to action
Content requirements:
• Clear presentation of two participation options:
1. Voucher Page (incentivised pricing)
2. Standard Advertising Page (no voucher)
• Simple comparison layout encouraged
Visual placeholders required:
• Space to show:
o A sample voucher page
o A sample advert-only page
Contact Details Area:
• VelaMarina logo or name
• Contact text placeholder (phone / email / website)
• Clean, professional call to action
Design Flexibility
We are happy to:
• Receive creative layout suggestions
• See optional icon sets
• See colour palette ideas
• Receive proposals that slightly refine the structure (as long as all elements are included)
Deliverables
• Final A5 4-page brochure design
• Print-ready PDF
• Editable source files (preferred)
• Clear indication of any optional extras (e.g. Passport cover design)
What We’re Looking For
• Clean layout
• Strong hierarchy
• Clear visual storytelling
• Understanding of hospitality / nightlife / tourism
• Ability to balance fun with professionalism
Optional Extras (welcome but not required)
• Proposal for the Passport front cover design
• Proposal for the transfer page design
• Icon set or mini graphic elements
• Alternative colour version
Notes to Designers
This brochure will be used repeatedly and updated over time, so clarity, flexibility, and strong structure are more important than heavy decoration.
We look forward to creative, thoughtful proposals.

Target Market(s)

LGBTIQ+ Tourists and Businesses

Industry/Entity Type

Tourism

Requirements
Must have
• meet the 4 page brief
Nice to have
• proposals for design elements within the design

```html
<!DOCTYPE html>
<html lang="en">
<head>
<meta charset="utf-8">
<title>VelaMarina Passport – A5 Brochure</title>
<link rel="stylesheet" href="https://fonts.googleapis.com/css2?family=Merriweather:ital,wght@0,400;0,700;0,900;1,700&family=Poppins:wght@400;500;600;700&display=swap">
<style>
  :root{
    --canvas:#e9e9eb;
    --paper:#ffffff;
    --cover-dark:#4a4543;
    --cover-mid:#6b6461;
    --navy:#2c2f6b;
    --gold:#f3c447;
    --brand-blue:#2a6fc9;
    --brand-yellow:#f2c12e;
    --coral:#ee7f67;
    --steel:#5aa7bf;
    --cream:#f3e7c4;
    --mint:#a6dccf;
    --sun-yellow:#f1c96e;
    --panel-grey:#dcdcde;
    --panel-beige:#f4efe3;
    --ink:#1e1e22;
    --muted:#8a8a90;
    --cross:#d7322b;
  }
  *{box-sizing:border-box;margin:0;padding:0}
  html,body{width:1200px;height:800px;overflow:hidden}
  body{background:var(--canvas);font-family:"Poppins",sans-serif;color:var(--ink);position:relative}

  .spread{position:absolute;top:202px;width:560px;height:396px;display:flex;box-shadow:0 6px 22px rgba(0,0,0,.12)}
  .spread--outer{left:26px}
  .spread--inner{left:614px}
  .page{position:relative;width:280px;height:396px;overflow:hidden;background:var(--paper)}

  /* Brand name lockup */
  .brand{display:flex;align-items:center;gap:5px;font-family:"Poppins",sans-serif;font-weight:700;color:var(--brand-blue);letter-spacing:.5px}
  .brand__dot{width:12px;height:12px;border-radius:50%;background:var(--brand-yellow);flex:none}

  /* Back cover */
  .offer-cards{position:absolute;top:22px;left:22px;right:22px;display:flex;gap:10px}
  .offer-card{flex:1;border-radius:16px;padding:14px 10px 16px;color:var(--ink);text-align:center;height:206px;display:flex;flex-direction:column;align-items:center}
  .offer-card--voucher{background:var(--coral)}
  .offer-card--advert{background:var(--steel);margin-top:22px}
  .offer-card__title{font-size:8px;font-weight:600;letter-spacing:.3px;line-height:1.3}
  .offer-card__text{font-size:5.5px;line-height:1.5;margin-top:8px;opacity:.8}
  .offer-card__sample{width:100%;height:40px;background:var(--cream);border-radius:4px;margin-top:14px;display:flex;align-items:center;justify-content:center}
  .offer-card__label{font-size:7px;font-weight:600;margin-top:8px;line-height:1.3}
  .contact{position:absolute;left:0;right:0;top:262px;text-align:center}
  .contact .brand{justify-content:center;font-size:17px}
  .contact__lines{margin-top:10px;font-size:7.5px;line-height:1.55;font-style:italic}

  /* Front cover */
  .cover{background:var(--cover-dark)}
  .cover__photo{position:absolute;inset:0;background:linear-gradient(160deg,#5b5553 0%,#3f3a39 55%,#2f2b2b 100%)}
  .cover__brand{position:absolute;top:24px;left:0;right:0;display:flex;justify-content:center}
  .cover__brand .brand{font-size:12px}
  .cover__title{position:absolute;top:52px;left:0;right:0;text-align:center;font-family:"Merriweather",serif;font-weight:900;color:#fff;font-size:28px;line-height:1.08}
  .cover__passport{position:absolute;top:178px;left:76px;width:128px;height:164px;background:var(--navy);border:2px solid var(--gold);border-radius:8px;box-shadow:0 0 14px rgba(243,196,71,.75)}
  .cover__art{position:absolute;top:16px;left:24px;width:76px;height:56px;border-radius:4px;background:linear-gradient(180deg,#f6c64a 0%,#f39a2a 55%,#4aa3d8 56%,#2c73b5 100%)}
  .cover__tagline{position:absolute;left:10px;right:10px;bottom:18px;text-align:center;font-family:"Merriweather",serif;font-style:italic;font-weight:700;color:#fff;font-size:8.5px;line-height:1.35}

  /* Inside left */
  .inside-left__photo{position:absolute;inset:0;background:linear-gradient(180deg,#9ccbe0 0%,#5fa6c7 30%,#d7c9a5 62%,#c9b387 100%)}
  .inside-left__brand{position:absolute;top:20px;right:14px}
  .inside-left__brand .brand{font-size:8px}
  .info-block{position:absolute;left:16px;right:16px;border-radius:14px;padding:12px 16px}
  .info-block--what{top:48px;background:var(--mint)}
  .info-block--benefits{top:200px;background:var(--sun-yellow)}
  .info-block__title{font-size:8.5px;font-weight:600;text-align:center;margin-bottom:8px;line-height:1.3}
  .info-list{list-style:none}
  .info-list li{display:flex;align-items:center;gap:8px;font-size:10px;font-weight:500;margin-bottom:6px}
  .info-list svg{flex:none}

  /* Inside right */
  .inside-right{background:#fafafa}
  .inside-right__brand{position:absolute;top:20px;right:14px}
  .inside-right__brand .brand{font-size:8px}
  .ownership{position:absolute;top:48px;left:12px;right:12px;height:118px;background:var(--panel-grey);border-radius:10px;padding:10px 8px;display:flex;gap:8px}
  .owner-card{flex:1;background:var(--paper);border-radius:6px;padding:7px 6px}
  .owner-card__title{font-size:6.5px;font-weight:600;text-align:center;line-height:1.25;margin-bottom:8px}
  .owner-card__field{font-size:5px;color:var(--muted);border-bottom:.6px solid #c9c9cd;padding-bottom:2px;margin-bottom:7px}
  .voucher-sample{position:absolute;left:12px;right:12px;top:236px;height:124px;background:var(--panel-beige);border-radius:10px}
  .voucher-sample__dot{position:absolute;left:22px;top:44px;width:30px;height:30px;border-radius:50%;background:var(--brand-yellow)}
  .voucher-sample__title{position:absolute;left:64px;top:34px;width:100px;text-align:center;font-family:"Merriweather",serif;font-size:10px;line-height:1.4;color:#3a3a48}
  .voucher-sample__box{position:absolute;right:22px;top:38px;width:52px;height:48px;background:#d5d5d7;border-radius:4px;display:flex;align-items:center;justify-content:center}
  .voucher-sample__tag{position:absolute;right:6px;top:-8px;width:18px;height:20px;background:var(--cross);border-radius:3px}
</style>
</head>
<body>

<section class="spread spread--outer" aria-label="Outer spread: back cover and front cover">
  <article class="page back-cover">
    <div class="offer-cards">
      <div class="offer-card offer-card--voucher">
        <h3 class="offer-card__title">VOUCHER PAGE</h3>
        <p class="offer-card__text">Feature your venue with an exclusive offer redeemed by passport holders in person.</p>
        <div class="offer-card__sample">
          <svg width="34" height="22" viewBox="0 0 34 22" aria-hidden="true"><rect x="2" y="3" width="30" height="16" rx="2" fill="none" stroke="#1e1e22" stroke-width="1.5"/><line x1="11" y1="3" x2="11" y2="19" stroke="#1e1e22" stroke-width="1.2" stroke-dasharray="2 2"/><line x1="15" y1="9" x2="28" y2="9" stroke="#1e1e22" stroke-width="1.2"/><line x1="15" y1="13" x2="24" y2="13" stroke="#1e1e22" stroke-width="1.2"/></svg>
        </div>
        <p class="offer-card__label">SAMPLE VOUCHER PAGE</p>
      </div>
      <div class="offer-card offer-card--advert">
        <h3 class="offer-card__title">STANDARD ADVERTISING PAGE</h3>
        <p class="offer-card__text">Showcase your venue with a full-page advert seen by high-spending visitors all season.</p>
        <div class="offer-card__sample">
          <svg width="30" height="22" viewBox="0 0 30 22" aria-hidden="true"><path d="M4 8h5l12-6v18L9 14H4z" fill="#fff" stroke="#1e1e22" stroke-width="1.4" stroke-linejoin="round"/><path d="M6 14l2 6h3l-1-6" fill="none" stroke="#1e1e22" stroke-width="1.3"/><path d="M24 7l3-2M24 11h4M24 15l3 2" stroke="#d7322b" stroke-width="1.3"/></svg>
        </div>
        <p class="offer-card__label">SAMPLE ADVERT-ONLY PAGE</p>
      </div>
    </div>
    <div class="contact">
      <div class="brand"><span class="brand__dot"></span>VelaMarina</div>
      <p class="contact__lines">Connect with VelaMarina<br>Phone: +00 000000000<br>Email: hello@velamarina.example<br>Website: www.velamarina.example<br>Join our network!</p>
    </div>
  </article>

  <article class="page cover">
    <div class="cover__photo" role="img" aria-label="Toned photo of a palm tree silhouette against a calm evening sea"></div>
    <div class="cover__brand"><div class="brand"><span class="brand__dot"></span>VelaMarina</div></div>
    <h1 class="cover__title">The<br>VelaMarina<br>Passport</h1>
    <div class="cover__passport">
      <div class="cover__art" role="img" aria-label="Passport cover illustration of a sun rising over the sea"></div>
      <p class="cover__tagline">A premium voucher booklet connecting tourists with local venues</p>
    </div>
  </article>
</section>

<section class="spread spread--inner" aria-label="Inner spread">
  <article class="page inside-left">
    <div class="inside-left__photo" role="img" aria-label="Photo of a busy sunny beach with turquoise sea"></div>
    <div class="inside-left__brand"><div class="brand"><span class="brand__dot"></span>VelaMarina</div></div>
    <div class="info-block info-block--what">
      <h2 class="info-block__title">What the VelaMarina<br>Passport is?</h2>
      <ul class="info-list">
        <li><svg width="12" height="10" viewBox="0 0 12 10" aria-hidden="true"><rect x="1" y="1" width="10" height="8" rx="1" fill="none" stroke="#1e1e22" stroke-width="1.2"/><line x1="4" y1="1" x2="4" y2="9" stroke="#1e1e22" stroke-dasharray="1.5 1.5"/></svg>Exclusive voucher</li>
        <li><svg width="12" height="10" viewBox="0 0 12 10" aria-hidden="true"><rect x="1" y="1" width="10" height="1.4" fill="#e40303"/><rect x="1" y="2.4" width="10" height="1.4" fill="#ff8c00"/><rect x="1" y="3.8" width="10" height="1.4" fill="#ffed00"/><rect x="1" y="5.2" width="10" height="1.4" fill="#008026"/><rect x="1" y="6.6" width="10" height="1.4" fill="#004dff"/><rect x="1" y="8" width="10" height="1.4" fill="#750787"/></svg>High-value LGBTQ+</li>
        <li><svg width="12" height="10" viewBox="0 0 12 10" aria-hidden="true"><rect x="2" y="2" width="8" height="7" fill="none" stroke="#1e1e22" stroke-width="1.2"/><path d="M1 3L6 0.5 11 3" fill="none" stroke="#1e1e22" stroke-width="1.2"/></svg>Connects with local venues</li>
      </ul>
    </div>
    <div class="info-block info-block--benefits">
      <h2 class="info-block__title">Key Benefits</h2>
      <ul class="info-list">
        <li><svg width="12" height="10" viewBox="0 0 12 10" aria-hidden="true"><circle cx="3.5" cy="3" r="1.6" fill="#1e1e22"/><circle cx="8.5" cy="3" r="1.6" fill="#1e1e22"/><path d="M0.5 9a3 3 0 016 0M5.5 9a3 3 0 016 0" fill="#1e1e22"/></svg>High-spending visitors</li>
        <li><svg width="12" height="10" viewBox="0 0 12 10" aria-hidden="true"><circle cx="6" cy="5" r="4" fill="none" stroke="#1e1e22" stroke-width="1.1"/><circle cx="6" cy="5" r="1.5" fill="#1e1e22"/></svg>Targeted reach</li>
        <li><svg width="12" height="10" viewBox="0 0 12 10" aria-hidden="true"><path d="M2 3h7l-2-2M10 7H3l2 2" fill="none" stroke="#1e1e22" stroke-width="1.2"/></svg>Transferable (up to 2 times)</li>
        <li><svg width="12" height="10" viewBox="0 0 12 10" aria-hidden="true"><rect x="1" y="2" width="10" height="7.5" rx="1" fill="#1e1e22"/><rect x="2.5" y="4" width="7" height="4" fill="#f1c96e"/></svg>No expiry date</li>
      </ul>
    </div>
  </article>

  <article class="page inside-right">
    <div class="inside-right__brand"><div class="brand"><span class="brand__dot"></span>VelaMarina</div></div>
    <div class="ownership">
      <div class="owner-card">
        <h3 class="owner-card__title">Original Passport<br>Owner</h3>
        <p class="owner-card__field">Name</p><p class="owner-card__field">Country</p><p class="owner-card__field">Signature</p><p class="owner-card__field">Date</p>
      </div>
      <div class="owner-card">
        <h3 class="owner-card__title">Transfer 1<br>New Owner</h3>
        <p class="owner-card__field">Name</p><p class="owner-card__field">Country</p><p class="owner-card__field">Signature</p><p class="owner-card__field">Date</p>
      </div>
      <div class="owner-card">
        <h3 class="owner-card__title">Transfer 2<br>Final Owner</h3>
        <p class="owner-card__field">Name</p><p class="owner-card__field">Country</p><p class="owner-card__field">Signature</p><p class="owner-card__field">Date</p>
      </div>
    </div>
    <div class="voucher-sample">
      <span class="voucher-sample__tag"></span>
      <span class="voucher-sample__dot"></span>
      <p class="voucher-sample__title">The VelaMarina Passport Vouchers</p>
      <div class="voucher-sample__box">
        <svg width="30" height="30" viewBox="0 0 30 30" aria-hidden="true"><path d="M5 5L25 25M25 5L5 25" stroke="var(--cross)" stroke-width="2.5" stroke-linecap="round"/></svg>
      </div>
    </div>
  </article>
</section>

</body>
</html>
```